Business Card Design

​Silver Harbor Rhythms provides personal, friendly service in a fun and high energy environment. We are based in Vermont.

We would like a card that appeals to a wide range of audiences as we do a wide range of events. Please feel free to check out our website silverharborrhythms.com for inspiration.

Target Market(s)

weddings, corporate, birthday parties, colleges

Industry/Entity Type

Business

Contact Information for Business Card

Silver Harbor Rhythms
Providing Entertainment For All Occasions
555 014 2968
silverharborrhythms@mailquill.net
silverharborrhythms.com

```html
<!DOCTYPE html>
<html lang="en">
<head>
<meta charset="utf-8">
<title>Silver Harbor Rhythms — Business Card</title>
<link href="https://fonts.googleapis.com/css2?family=Lato:wght@400;700;900&display=swap" rel="stylesheet">
<style>
  :root {
    --backdrop: #6b6b6b;
    --card-white: #ffffff;
    --brand-green: #2f5a28;
    --green-deep: #1c3d18;
    --green-light: #4a7a3a;
    --label-red: #b3242a;
    --ink: #2b2b2b;
    --swoosh-grey: #c9c9c9;
  }
  * { margin: 0; padding: 0; box-sizing: border-box; }
  html, body {
    width: 1200px;
    height: 900px;
    overflow: hidden;
    background: var(--backdrop);
    font-family: "Lato", Arial, sans-serif;
  }
  .business-card {
    position: absolute;
    left: 100px;
    top: 164px;
    width: 1000px;
    height: 572px;
    background: var(--card-white);
    overflow: hidden;
  }
  .green-wave {
    position: absolute;
    left: 0;
    top: 0;
    width: 1000px;
    height: 572px;
  }
  .brand-name {
    position: absolute;
    left: 110px;
    top: 145px;
    width: 380px;
    color: var(--brand-green);
    font-weight: 900;
    font-size: 44px;
    line-height: 1.1;
    text-transform: uppercase;
    letter-spacing: 1px;
  }
  .contact-list {
    position: absolute;
    left: 550px;
    top: 168px;
    list-style: none;
    font-size: 22px;
    line-height: 34px;
    color: var(--ink);
  }
  .contact-label {
    display: inline-block;
    width: 32px;
    color: var(--label-red);
  }
  .tagline {
    position: absolute;
    left: 30px;
    bottom: 34px;
    color: var(--card-white);
    font-size: 22px;
    letter-spacing: 1.4px;
    text-transform: uppercase;
  }
  .tagline-name { font-weight: 700; }
</style>
</head>
<body>
  <main class="business-card">
    <svg class="green-wave" viewBox="0 0 1000 572" aria-hidden="true">
      <defs>
        <linearGradient id="waveGreen" x1="0" y1="0" x2="1" y2="1">
          <stop offset="0" stop-color="var(--green-light)"/>
          <stop offset="1" stop-color="var(--green-deep)"/>
        </linearGradient>
      </defs>
      <path d="M0 392 C 150 420, 290 460, 420 452 C 600 440, 760 350, 1000 318 L 1000 572 L 0 572 Z" fill="url(#waveGreen)"/>
      <path d="M20 362 C 170 404, 300 440, 430 432 C 610 420, 770 328, 1000 298" fill="none" stroke="var(--swoosh-grey)" stroke-width="3"/>
    </svg>

    <div class="brand-name">Silver Harbor Rhythms</div>

    <ul class="contact-list">
      <li><span class="contact-label">P.</span>555 014 2968</li>
      <li><span class="contact-label">W.</span>silverharborrhythms.com</li>
      <li><span class="contact-label">E.</span>silverharborrhythms@mailquill.net</li>
    </ul>

    <p class="tagline"><span class="tagline-name">Silver Harbor Rhythms</span> Providing Entertainment For All Occasions</p>
  </main>
</body>
</html>
```